Hollow Lantern Distillery

I need a label designed for my small distillery. I’d like it to have a rose, and the name hollow lantern in script writing. I need the graphic to fit a standard gin bottle and I’ll need to be able to edit it depending on alcohol, warning and descriptions. I want it to look elegant and attractive, but slightly daring too. It’s a 700ml oslo bottle
Target Market(s)
Bespoke gin and vodka drinkers
Industry/Entity Type
Beverage
Font styles to use
Script
Other font styles liked:
- Something easy to read
Requirements
Must have
- Room for me to add and remove text depending on the drink
Nice to have
- Hollow lantern in script, slight colour on the rose and black writing

```html
<!DOCTYPE html>
<html lang="en">
<head>
<meta charset="utf-8">
<title>Hollow Lantern Rose Gin – Label Set</title>
<link href="https://fonts.googleapis.com/css2?family=Alex+Brush&family=Yellowtail&family=Libre+Baskerville&family=Oswald:wght@500&display=swap" rel="stylesheet">
<style>
  :root {
    --page: #ffffff;
    --paper: #f6f5f5;
    --paper-edge: #e4e2e3;
    --rose-line: #d48ca2;
    --rose-band: #d9a3b5;
    --rose-soft: #f1d3dc;
    --rose-wash: #efc4c8;
    --ink: #111111;
    --band-text: #ffffff;
  }
  * { box-sizing: border-box; margin: 0; padding: 0; }
  html, body {
    width: 1200px; height: 1200px; overflow: hidden;
    background: var(--page);
  }
  .label-set {
    position: relative; width: 1200px; height: 1200px;
    display: flex; justify-content: center; align-items: center; gap: 40px;
  }
  .label-group { display: flex; align-items: center; gap: 26px; }

  /* neck strip */
  .neck-strip {
    width: 70px; height: 330px;
    background: var(--paper);
    border: 1px solid var(--paper-edge);
    box-shadow: 0 2px 8px rgba(0,0,0,.08);
    position: relative;
    display: flex; align-items: center; justify-content: center;
  }
  .neck-strip::before, .neck-strip::after {
    content: ""; position: absolute; top: 0; bottom: 0; width: 2px; background: var(--rose-line);
  }
  .neck-strip::before { left: 7px; }
  .neck-strip::after { right: 7px; }
  .neck-name {
    writing-mode: vertical-rl; transform: rotate(180deg);
    font-family: "Alex Brush", cursive; font-size: 36px; color: var(--ink);
    white-space: nowrap;
  }

  /* front label */
  .front-label {
    position: relative; width: 440px; height: 580px;
    background: var(--paper);
    border: 1px solid var(--paper-edge);
    box-shadow: 0 3px 12px rgba(0,0,0,.08);
    overflow: hidden;
  }
  .label-frame {
    position: absolute; inset: 12px 10px 14px 10px;
    border: 2px solid var(--rose-line);
  }
  .watercolor-wash {
    position: absolute; left: 12px; top: 40px; width: 170px; height: 480px;
    background: radial-gradient(ellipse at 40% 30%, var(--rose-wash) 0%, rgba(239,196,200,.55) 35%, rgba(239,196,200,0) 72%),
                radial-gradient(ellipse at 70% 75%, rgba(239,196,200,.7) 0%, rgba(239,196,200,0) 60%);
    opacity: .8;
  }
  .brand-title {
    position: absolute; left: 0; right: 0; top: 64px;
    text-align: center; color: var(--ink);
  }
  .brand-title span { display: block; }
  .brand-title--flowing {
    font-family: "Alex Brush", cursive; font-size: 76px; line-height: 82px;
    text-shadow: 2px 3px 3px rgba(0,0,0,.25);
  }
  .brand-title--flowing .line-two { margin-left: -20px; }
  .brand-title--bold {
    top: 70px;
    font-family: "Yellowtail", cursive; font-size: 78px; line-height: 90px;
    text-shadow: 2px 3px 3px rgba(0,0,0,.22);
  }
  .rose-art {
    position: absolute; left: 52px; top: 262px; width: 336px; height: 158px;
    border-radius: 40px;
    background: radial-gradient(ellipse at 75% 45%, rgba(212,140,162,.45), rgba(241,211,220,.25) 55%, rgba(246,245,245,0) 80%),
                radial-gradient(ellipse at 30% 55%, rgba(212,140,162,.35), rgba(246,245,245,0) 70%);
  }
  .variety-band {
    position: absolute; left: 12px; right: 12px; top: 448px; height: 48px;
    background: var(--rose-band);
    display: flex; align-items: center; justify-content: center;
    font-family: "Libre Baskerville", serif; font-size: 25px; color: var(--band-text);
    letter-spacing: .5px;
  }
  .variety-band--pill {
    left: 212px; right: 10px; top: 446px; height: 44px;
    border-radius: 22px 0 0 22px;
  }
  .spec-line {
    position: absolute; left: 0; right: 0; top: 514px;
    text-align: center;
    font-family: "Oswald", sans-serif; font-weight: 500; font-size: 17px; color: var(--ink);
    letter-spacing: .2px;
  }
  .spec-line--right { left: 212px; right: 10px; top: 502px; }
</style>
</head>
<body>
<main class="label-set">

  <section class="label-group">
    <div class="neck-strip"><span class="neck-name">Hollow Lantern</span></div>
    <article class="front-label">
      <div class="watercolor-wash" role="img" aria-label="Soft pink watercolour wash"></div>
      <div class="label-frame"></div>
      <h1 class="brand-title brand-title--flowing">
        <span>Hollow</span>
        <span class="line-two">Lantern</span>
      </h1>
      <div class="rose-art" role="img" aria-label="Fine line drawing of roses with leaves and blossom sprigs in pink"></div>
      <div class="variety-band">ROSE GIN</div>
      <p class="spec-line">40% ABV &nbsp;|&nbsp; 700 ML</p>
    </article>
  </section>

  <section class="label-group">
    <div class="neck-strip"><span class="neck-name">Hollow Lantern</span></div>
    <article class="front-label">
      <div class="label-frame"></div>
      <h1 class="brand-title brand-title--bold">
        <span>Hollow</span>
        <span>Lantern</span>
      </h1>
      <div class="rose-art" role="img" aria-label="Fine line drawing of roses with leaves and blossom sprigs in pink"></div>
      <div class="variety-band variety-band--pill">ROSE GIN</div>
      <p class="spec-line spec-line--right">40% ABV &nbsp;|&nbsp; 700 ML</p>
    </article>
  </section>

</main>
</body>
</html>
```